Brochure design - Velto Rideshare community

We need a print ready brochure to tell drivers about the KRN community and the benefits of being a driver. We offer a alternative product to zandor and give drivers the ability to build their own customer base and build passive income. see design brief. check out our website www.krn-example.travel put in some good pics. Wanting a A4 Double sided brochure

Target Market(s)

Rideshare Drivers

Industry/Entity Type

Community

Font styles to use
Serif

Colors
00a990

Requirements
Must have
• clean design look. not too busy

```html
<!DOCTYPE html>
<html lang="en">
<head>
<meta charset="utf-8">
<title>KRN Driver Brochure – Cover Spread</title>
<link rel="stylesheet" href="https://fonts.googleapis.com/css2?family=Lora:wght@400;600;700&display=swap">
<style>
:root{
  --teal:#00a990;
  --teal-deep:#3f9a84;
  --ink:#161616;
  --slate:#5d6169;
  --slate-dark:#44474e;
  --paper:#ffffff;
  --stage:#2b2b2d;
  --muted:#555555;
  --tab:#2e3034;
}
*{box-sizing:border-box;margin:0;padding:0}
html,body{width:1200px;height:789px;overflow:hidden}
body{background:var(--stage);font-family:"Lora",Georgia,serif;position:relative}
.spread{position:absolute;left:105px;top:45px;width:990px;height:700px;display:flex;box-shadow:0 10px 30px rgba(0,0,0,.5)}
.page{position:relative;width:495px;height:700px;overflow:hidden;background:var(--paper)}
.overlay{position:absolute;inset:0;width:100%;height:100%}

/* shared brand lockup */
.brand{font-weight:700;color:var(--ink);display:flex;align-items:center;gap:10px;letter-spacing:1px}
.brand::before{content:"";width:11px;height:11px;border-radius:50%;background:var(--ink)}

/* back cover */
.about{position:absolute;left:0;top:0;width:100%;height:170px;background:linear-gradient(180deg,var(--slate-dark),var(--slate));color:#fff;padding:34px 36px 0;z-index:2}
.about-title{font-size:19px;font-weight:400;letter-spacing:.5px;padding-bottom:6px;border-bottom:1px solid rgba(255,255,255,.35);width:190px}
.about-title b{font-weight:700}
.about-text{font-size:10px;line-height:1.55;margin-top:9px;width:400px;opacity:.92}
.back-photo{position:absolute;left:0;top:170px;width:100%;height:440px;background:linear-gradient(160deg,#7d868c 0%,#a9b2a0 40%,#4b4f55 100%)}
.quote-band{position:absolute;left:-35px;top:372px;width:565px;height:76px;background:rgba(10,10,10,.88);transform:rotate(-14deg);display:flex;align-items:center;justify-content:center}
.quote-band p{color:#fff;font-weight:700;font-size:18px;line-height:1.3;text-align:center;letter-spacing:.5px}
.company-info{position:absolute;right:34px;bottom:118px;color:#fff;text-align:right;font-size:10.5px;line-height:1.65}
.company-info h3{font-size:12px;font-weight:700;border-bottom:1px solid rgba(255,255,255,.55);padding-bottom:4px;margin-bottom:4px}
.company-info .name{font-weight:700;letter-spacing:1px}
.back-brand{position:absolute;left:40px;bottom:38px;font-size:46px}

/* front cover */
.front-photo{position:absolute;left:0;top:140px;width:100%;height:380px;background:linear-gradient(150deg,#b9c2b4 0%,#8e9a86 45%,#5f6467 100%)}
.front-head{position:absolute;left:0;top:42px;width:100%;display:flex;flex-direction:column;align-items:center;gap:2px}
.front-brand{font-size:50px}
.front-sub{font-size:11px;letter-spacing:3px;color:var(--ink);padding-left:20px}
.tagline{position:absolute;right:34px;top:472px;text-align:right;font-size:16px;line-height:1.55;color:var(--muted);letter-spacing:.3px}
.tagline b{color:var(--teal-deep);font-weight:700}
.web-tab{position:absolute;right:0;top:562px;width:200px;height:36px;background:var(--tab);color:#fff;font-size:12px;display:flex;align-items:center;justify-content:center;gap:6px}
.web-tab b{color:var(--teal)}
.globe{width:11px;height:11px}
.abn{position:absolute;left:36px;bottom:12px;color:#fff;font-weight:700;font-size:12px;letter-spacing:.4px}
</style>
</head>
<body>
<div class="spread">

  <section class="page back-cover">
    <div class="back-photo" role="img" aria-label="Photo of a smiling rideshare driver chatting with a passenger in the car"></div>
    <div class="quote-band"><p>“DRIVE FOR YOURSELF,<br>NOT JUST FOR THE APP.”</p></div>
    <svg class="overlay" viewBox="0 0 495 700" preserveAspectRatio="none">
      <path d="M0 560 L495 432 V700 H0 Z" fill="var(--teal-deep)"/>
      <path d="M300 490 L495 439 V432 L300 483 Z" fill="var(--paper)"/>
    </svg>
    <div class="about">
      <h2 class="about-title">ABOUT <b>KRN</b></h2>
      <p class="about-text">At KRN, the journey matters. KRN is a community built for rideshare drivers – an alternative to zandor that lets you build your own customer base, keep more of every fare and grow passive income, on your terms.</p>
    </div>
    <div class="company-info">
      <h3>Join the Community</h3>
      <div class="name">RIDE ONWARD</div>
      <div>ABN: 12 345 678 901</div>
      <div>✉ info@krn-example.travel</div>
      <div>◍ www.krn-example.travel</div>
    </div>
    <div class="brand back-brand">KRN</div>
  </section>

  <section class="page front-cover">
    <div class="front-photo" role="img" aria-label="Photo of a smiling driver at the wheel of his car"></div>
    <svg class="overlay" viewBox="0 0 495 700" preserveAspectRatio="none">
      <path d="M0 0 H495 V150 Q260 170 0 250 Z" fill="var(--paper)"/>
      <path d="M0 250 Q260 170 495 150 V132 Q260 150 0 232 Z" fill="var(--teal-deep)"/>
      <path d="M0 700 V525 Q250 455 495 372 V700 Z" fill="var(--paper)"/>
      <path d="M0 525 Q250 455 495 372 V352 Q250 437 0 508 Z" fill="var(--teal-deep)"/>
      <path d="M0 700 V662 Q250 655 495 612 V700 Z" fill="var(--teal-deep)"/>
    </svg>
    <div class="front-head">
      <div class="brand front-brand">KRN</div>
      <div class="front-sub">RIDE ONWARD</div>
    </div>
    <p class="tagline">BE YOUR <b>OWN BOSS</b><br>BUILD YOUR <b>OWN CUSTOMER BASE</b><br>EARN REAL <b>PASSIVE INCOME</b></p>
    <div class="web-tab">
      <svg class="globe" viewBox="0 0 12 12"><circle cx="6" cy="6" r="5" fill="none" stroke="var(--teal)" stroke-width="1.2"/><path d="M1 6h10M6 1c2 2.5 2 7.5 0 10M6 1c-2 2.5-2 7.5 0 10" fill="none" stroke="var(--teal)" stroke-width="1"/></svg>
      <span>www.<b>krn-example</b>.travel</span>
    </div>
    <div class="abn">ABN: 12 345 678 901</div>
  </section>

</div>
</body>
</html>
```